Granite Ridge College-Pinecrest Welcome Week

I am the Student Activities Coordinator at Granite Ridge College-Pinecrest. For Welcome Week 2013, I need a standard poster 24x36 with the list of events happening. Our theme is based on the popular Friday Late Laughs video "We Got a Kite"
http://www.vidtrove.example/clip/Q4mZp8sLwTe
Our theme is:
We're at the 'Crest!
Welcome Week 2013
Graphics on the poster should reflect popular images/designs of FLL We Got a Kite. However, the boat should be a steamboat instead of the yacht image.
Unfortunately, I have a lot of text to fit on the poster. Traditionally we go with 3 margins listing events. I'm attaching the word document of events and our logo to this proposal. I'll also attach a few google images of "We Got a Kite" that align with the type of theme I'm looking for.
One last thing, our logo contains mountains listing all of the different campuses. Remove the campus names and mountains all together. Use simply the Colorado flag C and "Granite Ridge College".
Thanks for considering this brief!
Glen
Target Market(s)
Our college students love to ski and snowboard. In fact, one of our degrees is "Alpine Slope Commerce". Their ages are 18-22.
Industry/Entity Type
Events
Look and feel

```html
<!DOCTYPE html>
<html lang="en">
<head>
<meta charset="utf-8">
<title>Granite Ridge College-Pinecrest Welcome Week 2013</title>
<link href="https://fonts.googleapis.com/css2?family=Arimo:wght@700&family=Source+Sans+3:wght@400;600&display=swap" rel="stylesheet">
<style>
  :root {
    --page-bg: #e6e4e1;
    --poster-bg: #ffffff;
    --band: #0b0b0b;
    --band-text: #ffffff;
    --day-red: #b8323a;
    --event-navy: #27407e;
    --detail-grey: #3d3d3d;
    --water-deep: #1d3f73;
    --water-light: #5d86b4;
    --logo-box: #1c3a7a;
    --note-grey: #5b6a88;
  }
  * { margin: 0; padding: 0; box-sizing: border-box; }
  html, body {
    width: 834px; height: 1200px; overflow: hidden;
    background: var(--page-bg);
  }
  .poster {
    position: absolute; left: 27px; top: 15px;
    width: 780px; height: 1170px;
    background: var(--poster-bg);
    overflow: hidden;
    font-family: "Source Sans 3", "Myriad Pro", sans-serif;
  }
  .hero { position: absolute; left: 0; top: 0; width: 780px; height: 362px; }
  .brand {
    position: absolute; left: 531px; top: 14px; width: 224px; height: 112px;
    background: var(--logo-box);
    display: flex; align-items: center; justify-content: center; padding: 0 16px;
  }
  .brand-name {
    color: #ffffff; font-weight: 600; font-size: 24px; line-height: 1.05;
    text-transform: uppercase; letter-spacing: -0.3px; text-align: center;
  }
  .title-band {
    position: absolute; left: 0; top: 369px; width: 780px; height: 65px;
    background: var(--band); color: var(--band-text);
    font-family: "Arimo", Arial, sans-serif; font-weight: 700;
    display: flex; align-items: center; justify-content: center; gap: 14px;
    white-space: nowrap;
  }
  .title-theme { font-size: 32px; }
  .title-year { font-size: 54px; line-height: 1; }
  .day { position: absolute; width: 230px; }
  .day-name { color: var(--day-red); font-weight: 600; font-size: 15.5px; margin-bottom: 6px; }
  .event { margin-bottom: 10px; }
  .event-name { color: var(--event-navy); font-size: 12.5px; line-height: 15px; }
  .event-detail { color: var(--detail-grey); font-size: 11px; line-height: 13.5px; }
  .col-a { left: 62px; }
  .col-b { left: 308px; }
  .col-c { left: 530px; }
  .note {
    position: absolute; left: 530px; top: 1028px;
    color: var(--note-grey); font-size: 11px; line-height: 15px; text-transform: uppercase;
  }
  .steamboat {
    position: absolute; left: 505px; top: 1082px; width: 240px; height: 78px;
  }
</style>
</head>
<body>
<main class="poster">
  <svg class="hero" viewBox="0 0 780 362" role="img" aria-label="Photo of a white motor yacht speeding across deep blue water">
    <defs>
      <linearGradient id="water" x1="0" y1="0" x2="1" y2="1">
        <stop offset="0" stop-color="var(--water-light)"/>
        <stop offset="1" stop-color="var(--water-deep)"/>
      </linearGradient>
    </defs>
    <path d="M0 0 H780 V230 Q560 370 390 360 Q200 352 0 262 Z" fill="url(#water)"/>
  </svg>

  <div class="brand">
    <span class="brand-name">Granite Ridge College</span>
  </div>

  <h1 class="title-band">
    <span class="title-theme">We're at the 'Crest! Welcome Week</span>
    <span class="title-year">2013</span>
  </h1>

  <section class="day col-a" style="top:458px">
    <h2 class="day-name">Thursday August 22</h2>
    <div class="event"><p class="event-name">Residence Hall Move-In</p><p class="event-detail">12:00pm-3:00pm<br>Ridge Hall</p></div>
    <div class="event"><p class="event-name">Brunch</p><p class="event-detail">10:00am-1:00pm<br>Dining Hall</p></div>
    <div class="event"><p class="event-name">International Students Orientation</p><p class="event-detail">3:00pm<br>Aldridge 121</p></div>
    <div class="event"><p class="event-name">Dinner</p><p class="event-detail">5:00pm-6:30pm<br>Dining Hall<br>Warm Springs Waterslide Party<br>7:00pm-9:00pm<br>Old Mill Warm Springs</p></div>
  </section>

  <section class="day col-a" style="top:800px">
    <h2 class="day-name">Friday August 23</h2>
    <div class="event"><p class="event-name">Breakfast</p><p class="event-detail">7:30am-9:00am<br>Dining Hall</p></div>
    <div class="event"><p class="event-name">Hike Cedar Creek Falls</p><p class="event-detail">9:00am-11:30am<br>Shuttle leaves Ridge Hall at 8:30am</p></div>
    <div class="event"><p class="event-name">BBQ and Faculty Ice Cream Social</p><p class="event-detail">12:00pm-1:30pm<br>Dining Hall</p></div>
    <div class="event"><p class="event-name">Kick Off Party: Inflatables</p><p class="event-detail">1:30pm-4:00pm<br>Upper Parking Lot</p></div>
    <div class="event"><p class="event-name">Dinner</p><p class="event-detail">5:00pm-6:00pm<br>Dining Hall</p></div>
    <div class="event"><p class="event-name">Free Concert</p><p class="event-detail">7:00pm<br>Pinecrest Resort Base<br>(PTB Buses to Resort,<br>5:35pm Last Bus)</p></div>
  </section>

  <section class="day col-b" style="top:458px">
    <h2 class="day-name">Saturday August 24</h2>
    <div class="event"><p class="event-name">Main Street Farmers Market</p><p class="event-detail">9:00am-2:00pm<br>6th &amp; Aspen (walking dist.)</p></div>
    <div class="event"><p class="event-name">Brunch</p><p class="event-detail">10:00am-1:00pm<br>Dining Hall</p></div>
    <div class="event"><p class="event-name">Cedar Grove Warm Springs</p><p class="event-detail">2:00pm-5:00pm<br>Shuttle leaves Ridge Hall at 1:30pm</p></div>
    <div class="event"><p class="event-name">Dinner</p><p class="event-detail">5:00-6:00pm<br>Dining Hall</p></div>
    <div class="event"><p class="event-name">Free Movie on the Mountain:<br>Arena Trials</p><p class="event-detail">8:00pm<br>(PTB Buses to Resort,<br>5:35pm Last Bus)</p></div>
  </section>

  <section class="day col-b" style="top:800px">
    <h2 class="day-name">Sunday August 25</h2>
    <div class="event"><p class="event-name">Brunch</p><p class="event-detail">10:00am-1:00pm<br>Dining Hall</p></div>
    <div class="event"><p class="event-name">Alpine Slide/Volleyball</p><p class="event-detail">2:00pm-4:00pm<br>Meet at Tallpine Hill</p></div>
    <div class="event"><p class="event-name">Dinner</p><p class="event-detail">5:00pm-6:00pm<br>Dining Hall</p></div>
    <div class="event"><p class="event-name">Mandatory All Hall Meeting</p><p class="event-detail">6:00pm<br>Auditorium</p></div>
    <div class="event"><p class="event-name">RHA Super Sunday Program</p><p class="event-detail">8:00pm<br>Ridge Hall: MPR</p></div>
  </section>

  <section class="day col-c" style="top:458px">
    <h2 class="day-name">Monday August 26</h2>
    <div class="event"><p class="event-name">Regular Dining Hall Hours Begin</p></div>
    <div class="event"><p class="event-detail">“Being Alone Sucks!”<br>9:00pm<br>Auditorium</p></div>
  </section>

  <section class="day col-c" style="top:566px">
    <h2 class="day-name">Tuesday August 27</h2>
    <div class="event"><p class="event-name">Newly Roommate Game</p><p class="event-detail">7:00pm-8:00pm<br>Ridge Hall: MPR</p></div>
    <div class="event"><p class="event-name">Free Gelato</p><p class="event-detail">8:00pm-9:00pm<br>Dolce Gelato 7th and Birch</p></div>
  </section>

  <section class="day col-c" style="top:708px">
    <h2 class="day-name">Wednesday August 28</h2>
    <div class="event"><p class="event-name">Free Bowling</p><p class="event-detail">9:00pm<br>Summit Lanes</p></div>
  </section>

  <section class="day col-c" style="top:800px">
    <h2 class="day-name">Thursday August 29</h2>
    <div class="event"><p class="event-name">Club Fair</p><p class="event-detail">10:00am-2:00pm<br>Dining Hall</p></div>
    <div class="event"><p class="event-name">Black Light Dodgeball</p><p class="event-detail">9:00pm<br>Gym</p></div>
  </section>

  <section class="day col-c" style="top:938px">
    <h2 class="day-name">Friday August 30</h2>
    <div class="event"><p class="event-name">Late Night Climbing</p><p class="event-detail">9:00pm<br>Gym</p></div>
  </section>

  <p class="note">All events *<br>are free<br>unless otherwise noted</p>

  <svg class="steamboat" viewBox="0 0 240 78" role="img" aria-label="Faint illustration of a paddle steamboat">
    <defs>
      <linearGradient id="steam" x1="0" y1="0" x2="0" y2="1">
        <stop offset="0" stop-color="#f4f5f7"/>
        <stop offset="1" stop-color="#d9dde3"/>
      </linearGradient>
    </defs>
    <rect x="0" y="0" width="240" height="78" rx="6" fill="url(#steam)"/>
  </svg>
</main>
</body>
</html>
```